Business card design for event company

need design double sided in square shape ( approx 6x6cm) in matt grey shades
front side :
logo ( could be in one color like picture attached ) printpress effect in a rect box

back side :
name in big font with silver foil finish ( similar to attached pic )

phone number i would like to see how it will look like if embossed ( like in credit cards )

Sample for contact on card ( will need 5 different contacts) - pls. include small icons next to each contact

WALEED RAFIQI
Managing Director

+971 50 317 6490
waleed@loomcrestuae.com
www.loomcrest.ae
Building C2 , Office 713
Dubai Saffron Heights

Please consider this is an urgent project . thank you in advance

```html
<!DOCTYPE html>
<html lang="en">
<head>
<meta charset="utf-8">
<title>Loomcrest – Business Card</title>
<link rel="stylesheet" href="https://fonts.googleapis.com/css2?family=Montserrat:wght@400;600&family=Source+Sans+3:wght@400&display=swap">
<style>
  :root {
    --stage: #2d2d2d;
    --card-dark: #141414;
    --card-light: #e4e4e4;
    --silver: #8c8c8c;
    --silver-light: #a9a9a9;
    --accent: #e08a2e;
    --text-muted: #8e8e8e;
    --ink-dark: #444444;
  }
  * { margin: 0; padding: 0; box-sizing: border-box; }
  html, body { width: 1200px; height: 900px; overflow: hidden; background: var(--stage); }
  .canvas { position: relative; width: 1200px; height: 900px; }
  .card {
    position: absolute;
    top: 247px;
    width: 392px;
    height: 399px;
  }
  .card--front { left: 175px; background: var(--card-dark); }
  .card--back { left: 658px; background: var(--card-light); }

  .brand {
    font-family: "Montserrat", sans-serif;
    font-weight: 400;
    white-space: nowrap;
    display: flex;
    align-items: center;
  }
  .brand__dot { display: inline-block; width: 8px; height: 8px; margin-right: 8px; }
  .card--front .brand {
    position: absolute; right: 22px; top: 52px;
    font-size: 26px; color: var(--silver);
  }
  .card--front .brand__dot { background: var(--silver); }
  .card--back .brand {
    position: absolute; left: 0; right: 0; top: 172px;
    justify-content: center;
    font-size: 40px; color: var(--ink-dark);
  }
  .card--back .brand__dot { background: var(--ink-dark); width: 10px; height: 10px; }

  .person { position: absolute; left: 17px; top: 200px; }
  .person__name {
    font-family: "Montserrat", sans-serif;
    font-size: 23px; letter-spacing: 0.3px;
    color: var(--silver-light);
  }
  .person__name strong { font-weight: 600; color: var(--silver); }
  .person__name span { font-weight: 400; }
  .person__role {
    margin-top: 4px;
    font-family: "Montserrat", sans-serif;
    font-size: 15px; font-weight: 400;
    color: var(--accent);
  }

  .contacts { position: absolute; left: 17px; top: 312px; list-style: none; }
  .contacts__item {
    display: flex; align-items: center;
    height: 30px;
    font-family: "Source Sans 3", sans-serif;
    font-size: 16px;
    color: var(--text-muted);
  }
  .contacts__icon { width: 15px; height: 15px; margin-right: 13px; fill: var(--accent); flex: none; }

  .website {
    position: absolute; left: 0; right: 0; top: 278px;
    text-align: center;
    font-family: "Montserrat", sans-serif;
    font-weight: 600; font-size: 14px; letter-spacing: 2.4px;
    color: var(--ink-dark);
  }
</style>
</head>
<body>
<main class="canvas">
  <section class="card card--front" aria-label="Card front with contact details">
    <div class="brand"><i class="brand__dot"></i>Loomcrest</div>
    <div class="person">
      <h1 class="person__name"><strong>WALEED</strong> <span>RAFIQI</span></h1>
      <p class="person__role">MANAGING DIRECTOR</p>
    </div>
    <ul class="contacts">
      <li class="contacts__item">
        <svg class="contacts__icon" viewBox="0 0 16 16" aria-hidden="true"><path d="M1 5c0-2 3-3 7-3s7 1 7 3v1h-4V5H5v1H1z"/><path d="M3 8h10l1 6H2z"/><circle cx="8" cy="11" r="1.6" fill="#141414"/></svg>
        +971 50 317 6490
      </li>
      <li class="contacts__item">
        <svg class="contacts__icon" viewBox="0 0 16 16" aria-hidden="true"><path d="M1 3h14v10H1z"/><path d="M1.5 3.5 8 9l6.5-5.5" fill="none" stroke="#141414" stroke-width="1.4"/></svg>
        waleed@loomcrestuae.com
      </li>
      <li class="contacts__item">
        <svg class="contacts__icon" viewBox="0 0 16 16" aria-hidden="true"><path d="M8 1a5 5 0 0 1 5 5c0 4-5 9-5 9S3 10 3 6a5 5 0 0 1 5-5z"/><circle cx="8" cy="6" r="1.8" fill="#141414"/></svg>
        Building C2 , Office 713, Dubai Saffron Heights
      </li>
    </ul>
  </section>

  <section class="card card--back" aria-label="Card back with company name">
    <div class="brand"><i class="brand__dot"></i>Loomcrest</div>
    <p class="website">www.loomcrest.ae</p>
  </section>
</main>
</body>
</html>
```